Heronwick Lodge Sign

Heronwick Lodge is a lake resort in Branson, MO
This resort used to have 66 units however the resort was sold in sections. I own the part of the resort that has all the amenities listed on the attached file. We need an updated sign and also billboard.
On a sign like this should be include a phone number?

```html
<!DOCTYPE html>
<html lang="en">
<head>
<meta charset="utf-8">
<title>Heronwick Lodge Sign</title>
<link href="https://fonts.googleapis.com/css2?family=Jost:wght@400;500;600;700&display=swap" rel="stylesheet">
<style>
  :root {
    --navy: #253d8c;
    --green: #7ab642;
    --sun: #f7e23a;
    --white: #ffffff;
    --backdrop: #e9ebee;
  }
  html, body {
    margin: 0;
    padding: 0;
    width: 1200px;
    height: 960px;
    overflow: hidden;
    background: var(--backdrop);
    font-family: "Jost", sans-serif;
  }
  .sign {
    position: absolute;
    left: 53px;
    top: 62px;
    width: 1094px;
    height: 836px;
    background: var(--white);
    overflow: hidden;
    box-shadow: 0 2px 10px rgba(0,0,0,0.12);
  }
  .sign__waves {
    position: absolute;
    inset: 0;
    width: 1094px;
    height: 836px;
  }
  .brand {
    position: absolute;
    top: 148px;
    left: 0;
    width: 100%;
    text-align: center;
  }
  .brand__name {
    font-size: 84px;
    font-weight: 600;
    color: var(--navy);
    line-height: 1;
    letter-spacing: -0.5px;
  }
  .brand__tagline {
    margin-top: 14px;
    font-size: 42px;
    font-weight: 400;
    color: var(--navy);
    line-height: 1;
  }
  .amenities {
    position: absolute;
    top: 334px;
    margin: 0;
    padding: 0;
    list-style: none;
    font-size: 27px;
    font-weight: 600;
    color: var(--navy);
    line-height: 35px;
  }
  .amenities li::before {
    content: "";
    display: inline-block;
    width: 8px;
    height: 8px;
    border-radius: 50%;
    background: var(--green);
    margin-right: 10px;
    vertical-align: middle;
    position: relative;
    top: -2px;
  }
  .amenities--left { left: 46px; }
  .amenities--right { left: 598px; }
  .amenities__divider {
    position: absolute;
    left: 512px;
    top: 342px;
    width: 4px;
    height: 272px;
    background: var(--green);
  }
  .contact {
    position: absolute;
    left: 30px;
    right: 36px;
    top: 735px;
    display: flex;
    align-items: baseline;
    justify-content: space-between;
    color: var(--white);
    font-weight: 600;
  }
  .contact__address,
  .contact__web {
    font-size: 30px;
  }
  .contact__phone {
    font-size: 58px;
    font-weight: 700;
    color: var(--sun);
    letter-spacing: 0.5px;
  }
</style>
</head>
<body>
  <div class="sign">
    <svg class="sign__waves" viewBox="0 0 1094 836" aria-hidden="true">
      <path d="M0 662 C 180 618, 360 684, 547 650 S 900 618, 1094 654" fill="none" stroke="var(--green)" stroke-width="6"/>
      <path d="M0 684 C 180 640, 360 706, 547 672 S 900 640, 1094 676 V836 H0 Z" fill="var(--navy)"/>
    </svg>

    <header class="brand">
      <div class="brand__name">Heronwick Lodge</div>
      <div class="brand__tagline">on Table Rock Lake</div>
    </header>

    <ul class="amenities amenities--left">
      <li>Direct Lake access</li>
      <li>Swim Decks</li>
      <li>Slip Rentals</li>
      <li>Boat Rentals</li>
      <li>Indoor Pool</li>
      <li>Golf Carts</li>
      <li>Pantoon Boats</li>
      <li>Kayak - Paddleboards</li>
    </ul>
    <div class="amenities__divider"></div>
    <ul class="amenities amenities--right">
      <li>1-3 Bedroom Vacation Rentals</li>
      <li>Dining Hall</li>
      <li>Game Room</li>
      <li>Children’s Activities</li>
      <li>Pet Friendly</li>
      <li>Gift Store</li>
      <li>Outdoor Games</li>
      <li>Family Reunions - Large Groups</li>
    </ul>

    <footer class="contact">
      <span class="contact__address">218 Willow Bend</span>
      <span class="contact__phone">800-555-0142</span>
      <span class="contact__web">Heronwicklodge.com</span>
    </footer>
  </div>
</body>
</html>
```